Tallgrove Vale Management

I need a professional website. My current website is tallgrovevalemanagement.com and I hate it. It was created with some AI tool very quickly because I needed a site up and running with no advanced notice. I’m open to all designs .. I trust you, the professionals will deliver the results I’m anxiously awaiting! :)

```html
<!DOCTYPE html>
<html lang="en">
<head>
<meta charset="utf-8">
<title>Tallgrove Vale Management — Property Management</title>
<link rel="stylesheet" href="https://fonts.googleapis.com/css2?family=Fraunces:opsz,wght@9..144,700;9..144,800&family=Inter:wght@400;500;600;700;800&display=swap">
<style>
:root{
  --navy:#1a2947;
  --navy-deep:#13203a;
  --navy-mid:#2a4272;
  --red:#d8252b;
  --red-deep:#b3151f;
  --paper:#f3f5f8;
  --white:#ffffff;
  --ink:#1a2947;
  --muted:#5a6478;
  --line:#dde2ea;
  --green:#1f8a4c;
}
*{box-sizing:border-box;margin:0;padding:0}
html,body{width:1200px;height:3734px;overflow:hidden}
body{font-family:"Inter",Arial,sans-serif;color:var(--ink);background:var(--white)}
.serif{font-family:"Fraunces",Georgia,serif;font-weight:800;letter-spacing:-.5px}
.eyebrow{font-size:8px;font-weight:800;letter-spacing:1.3px;text-transform:uppercase;color:var(--red)}
.wrap{position:relative}

/* nav */
.nav{height:52px;background:#eef1f5;display:flex;align-items:center;justify-content:space-between;padding:0 44px;position:relative;z-index:2}
.brand{display:flex;align-items:center;gap:10px;font-weight:800;font-size:11px;line-height:1.05;text-transform:uppercase;color:var(--navy)}
.brand-dot{width:30px;height:30px;border-radius:50%;background:var(--navy)}
.nav-links{display:flex;align-items:center;gap:20px;font-size:10px;font-weight:600;color:var(--navy)}
.btn{display:inline-block;font-size:8.5px;font-weight:800;letter-spacing:.6px;text-transform:uppercase;padding:10px 14px}
.btn-red{background:var(--red);color:var(--white)}
.btn-white{background:var(--white);color:var(--navy)}

/* hero */
.hero{height:628px;position:relative;overflow:hidden}
.hero-photo{position:absolute;inset:0;background:linear-gradient(110deg,#1c3358 0%,#2c4a74 35%,#6b7f92 60%,#9a8e80 80%,#5e6e60 100%)}
.hero-shade{position:absolute;inset:0;background:linear-gradient(90deg,rgba(22,36,66,.92) 0%,rgba(22,36,66,.6) 45%,rgba(22,36,66,.1) 100%)}
.hero-copy{position:absolute;left:52px;top:106px;color:var(--white)}
.hero-copy h1{font-size:72px;line-height:80px;margin-top:10px}
.hero-copy p{font-size:14px;line-height:22.5px;width:440px;margin-top:18px;color:#e6eaf2}
.hero-actions{display:flex;gap:10px;margin-top:22px}
.snapshot{position:absolute;left:955px;top:462px;width:194px;height:124px;background:var(--paper);border-top:4px solid var(--red);padding:18px 17px}
.snapshot .label{font-size:7px;font-weight:800;letter-spacing:1px;color:var(--muted)}
.snapshot .big{font-size:42px;font-weight:700;color:var(--navy);line-height:1;margin:6px 0 6px}
.snapshot .small{font-size:9.5px;line-height:14px;color:var(--muted)}

/* strip */
.strip{height:81px;display:flex;border-bottom:1px solid var(--line)}
.strip div{flex:1;padding:25px 43px;border-right:1px solid var(--line)}
.strip b{display:block;font-size:13.5px;color:var(--navy);margin-bottom:6px}
.strip span{font-size:10px;color:var(--muted)}

/* owners */
.owners{height:337px;background:var(--paper);display:flex;padding:90px 52px 0}
.owners h2{font-size:46px;line-height:45px;width:600px;margin-top:6px}
.owners .col-r{margin-left:64px;padding-top:22px;width:430px;font-size:11px;line-height:19px;color:var(--muted)}
.owners .col-r p+p{margin-top:12px}

/* services */
.services{height:500px;padding:92px 52px 0}
.sec-head{display:flex}
.sec-head .eyebrow{width:357px;padding-top:4px}
.sec-head h2{font-size:46px;line-height:45px}
.cards{display:flex;margin-top:36px;border:1px solid var(--line);height:199px}
.card{flex:1;padding:20px 19px;border-right:1px solid var(--line)}
.card:last-child{border-right:0}
.num{width:25px;height:25px;border-radius:50%;border:1px solid #f0c4c6;color:var(--red);font-size:7.5px;font-weight:700;display:flex;align-items:center;justify-content:center}
.card h3{font-size:15px;font-weight:700;margin:28px 0 10px}
.card p{font-size:10px;line-height:16px;color:var(--muted)}

/* clarity band */
.clarity{height:423px;background:linear-gradient(110deg,#2b4676 0%,#1c2d52 70%,#172644 100%);position:relative}
.clarity .copy{position:absolute;left:52px;top:162px;color:var(--white)}
.clarity h2{font-size:46px;line-height:45px;width:800px;margin-top:2px}
.pulse-back{position:absolute;left:860px;top:74px;width:300px;height:300px;background:var(--red)}
.pulse{position:absolute;left:848px;top:60px;width:300px;height:304px;background:var(--white);padding:18px 18px}
.pulse-top{display:flex;justify-content:space-between;font-size:7.5px;font-weight:800;letter-spacing:.8px;padding-bottom:12px;border-bottom:1px solid var(--line)}
.pulse-top .ok{color:var(--green);letter-spacing:0;font-size:9.5px;font-weight:700}
.row{display:flex;justify-content:space-between;align-items:center;height:45px;border-bottom:1px solid var(--line);font-size:10px;color:var(--muted)}
.row b{font-size:16px;color:var(--navy)}
.bars{margin-top:24px}

/* process */
.process{height:484px;background:var(--paper);padding:94px 52px 0}
.steps{display:flex;border-top:2px solid #4a5670;margin-top:38px}
.step{flex:1;padding:28px 0 0;border-right:1px solid var(--line);height:138px}
.step:last-child{border-right:0}
.step .n{font-size:10px;font-weight:700;color:var(--red)}
.step h3{font-size:19px;font-weight:700;margin:20px 0 9px}
.step p{font-size:10px;line-height:16px;color:var(--muted);width:250px}

/* quote */
.quote{height:386px;background:var(--red-deep);padding:62px 52px 0}
.quote blockquote{font-size:52px;line-height:50px;color:var(--white);width:680px}

/* contact */
.contact{height:582px;display:flex;padding:87px 54px 0 52px}
.contact .left{width:555px}
.contact h2{font-size:46px;line-height:45px;width:420px;margin-top:2px}
.contact .lede{font-size:11px;line-height:19px;color:var(--muted);width:310px;margin-top:22px}
.contact .mail{display:inline-block;margin-top:16px;font-size:10.5px;font-weight:600;color:var(--navy);border-bottom:2px solid var(--red);padding-bottom:1px}
.form{width:539px;height:407px;border:1px solid var(--line);border-top:4px solid var(--navy);background:var(--paper);padding:24px 27px}
.form label{display:block;font-size:7.5px;font-weight:800;letter-spacing:.8px;margin-bottom:9px}
.field{height:31px;background:var(--white);border:1px solid #cfd5df;font-size:8px;font-weight:600;color:var(--muted);padding:10px 10px;margin-bottom:17px}
.field.tall{height:86px}
.submit{height:28px;background:var(--red);color:var(--white);font-size:8px;font-weight:800;letter-spacing:.5px;text-align:center;line-height:28px;margin-top:-4px}
.note{font-size:8px;color:var(--muted);margin-top:11px}

/* footer */
.footer{height:261px;background:var(--navy-deep);color:#cfd6e4;padding:34px 52px 0;position:relative}
.footer .fbrand{display:flex;align-items:center;gap:10px;font-family:"Inter",Arial,sans-serif;font-weight:800;font-size:14px;color:var(--white);height:70px}
.footer .fbrand i{width:22px;height:22px;background:var(--white);display:block}
.footer .tag{font-size:10px;line-height:16px;margin-top:28px;width:230px}
.fcol{position:absolute;top:40px;font-size:10px;line-height:23px}
.fcol h4{font-size:7.5px;font-weight:800;letter-spacing:1px;color:var(--white);margin-bottom:2px}
.fbottom{position:absolute;left:52px;right:52px;top:215px;border-top:1px solid #2c3a58;padding-top:14px;font-size:7.5px;color:#9aa5bb}
</style>
</head>
<body>

<header class="nav">
  <div class="brand"><span class="brand-dot"></span><span>Tallgrove Vale<br>Management</span></div>
  <nav class="nav-links">
    <span>Services</span><span>Owners</span><span>Process</span><span>Contact</span>
    <span class="btn btn-red">Request proposal</span>
  </nav>
</header>

<section class="hero">
  <div class="hero-photo" role="img" aria-label="Photo of a white two-storey home with wraparound balconies, a pool and palm fronds"></div>
  <div class="hero-shade"></div>
  <div class="hero-copy">
    <div class="eyebrow">Cleveland · Akron · Property management</div>
    <h1 class="serif">A true<br>partner in<br>property<br>performance.</h1>
    <p>Tallgrove Vale Management protects asset value, improves resident experience, and gives owners a clearer operating picture across every door.</p>
    <div class="hero-actions">
      <span class="btn btn-red">Start a consultation</span>
      <span class="btn btn-white">Explore services</span>
    </div>
  </div>
  <div class="snapshot">
    <div class="label">PORTFOLIO SNAPSHOT</div>
    <div class="big">96%</div>
    <div class="small">target occupancy focus with responsive tenant care</div>
  </div>
</section>

<section class="strip">
  <div><b>Local</b><span>Cleveland and Akron market knowledge</span></div>
  <div><b>Disciplined</b><span>Documented processes and reporting</span></div>
  <div><b>Responsive</b><span>Owner and tenant communication</span></div>
</section>

<section class="owners">
  <div>
    <div class="eyebrow">Built for owners</div>
    <h2 class="serif">Asset preservation with the urgency of day-to-day management.</h2>
  </div>
  <div class="col-r">
    <p>Professional management should do more than collect rent. It should reduce surprises, coordinate maintenance before issues compound, and keep every stakeholder informed.</p>
    <p>Tallgrove Vale Management brings structure to residential portfolios, rentals, and investor-owned assets throughout Northeast Ohio.</p>
  </div>
</section>

<section class="services">
  <div class="sec-head">
    <div class="eyebrow">Management services</div>
    <h2 class="serif">Everything needed to operate<br>property with confidence.</h2>
  </div>
  <div class="cards">
    <div class="card"><div class="num">01</div><h3>Leasing &amp; Placement</h3><p>Market-ready preparation, qualified resident placement, lease coordination, and move-in communication.</p></div>
    <div class="card"><div class="num">02</div><h3>Maintenance Oversight</h3><p>Responsive work order handling, vendor coordination, and practical repair decisions that preserve long-term value.</p></div>
    <div class="card"><div class="num">03</div><h3>Rent &amp; Reporting</h3><p>Clear owner updates, rent collection workflows, expense visibility, and performance summaries.</p></div>
    <div class="card"><div class="num">04</div><h3>Tenant Experience</h3><p>Professional communication and dependable support that helps residents feel heard and homes stay cared for.</p></div>
  </div>
</section>

<section class="clarity">
  <div class="copy">
    <div class="eyebrow">Operational clarity</div>
    <h2 class="serif">Know what is happening before it becomes expensive.</h2>
  </div>
  <div class="pulse-back"></div>
  <div class="pulse">
    <div class="pulse-top"><span>JULY PORTFOLIO PULSE</span><span class="ok">On track</span></div>
    <div class="row"><span>Open work orders</span><b>7</b></div>
    <div class="row"><span>Avg response time</span><b>2.4h</b></div>
    <div class="row"><span>Upcoming renewals</span><b>12</b></div>
    <svg class="bars" width="264" height="74" viewBox="0 0 264 74" aria-hidden="true">
      <defs><linearGradient id="barFill" x1="0" y1="0" x2="0" y2="1"><stop offset="0" stop-color="#d8252b"/><stop offset="1" stop-color="#2a3d68"/></linearGradient></defs>
      <rect x="0" y="24" width="46" height="50" fill="url(#barFill)"/>
      <rect x="54" y="6" width="46" height="68" fill="url(#barFill)"/>
      <rect x="109" y="16" width="46" height="58" fill="url(#barFill)"/>
      <rect x="163" y="0" width="46" height="74" fill="url(#barFill)"/>
      <rect x="218" y="14" width="46" height="60" fill="url(#barFill)"/>
    </svg>
  </div>
</section>

<section class="process">
  <div class="sec-head">
    <div class="eyebrow">How engagement starts</div>
    <h2 class="serif">A practical path from first<br>conversation to active<br>management.</h2>
  </div>
  <div class="steps">
    <div class="step"><div class="n">01</div><h3>Assess</h3><p>Discuss the property, current pain points, goals, and management needs.</p></div>
    <div class="step"><div class="n">02</div><h3>Plan</h3><p>Build a tailored proposal around scope, communication rhythm, and priorities.</p></div>
    <div class="step"><div class="n">03</div><h3>Stabilize</h3><p>Organize records, vendor handoffs, tenant communication, and maintenance workflows.</p></div>
    <div class="step"><div class="n">04</div><h3>Improve</h3><p>Track performance, prevent avoidable issues, and refine operations over time.</p></div>
  </div>
</section>

<section class="quote">
  <blockquote class="serif">“The right manager should feel like an extension of ownership: accountable, informed, and calm under pressure.”</blockquote>
</section>

<section class="contact">
  <div class="left">
    <div class="eyebrow">Request a tailored proposal</div>
    <h2 class="serif">Bring structure to your property operations.</h2>
    <p class="lede">Tell Tallgrove Vale Management what you own, where it is located, and what you need improved. The next step is a consultative assessment.</p>
    <span class="mail">info@tallgrovevalemanagement.com</span>
  </div>
  <div class="form">
    <label>FULL NAME</label><div class="field">Your name</div>
    <label>EMAIL ADDRESS</label><div class="field">you@example.com</div>
    <label>PROPERTY LOCATION</label><div class="field">Cleveland, Akron, or nearby</div>
    <label>HOW CAN WE HELP?</label><div class="field tall">Tell us about the property, portfolio size, or current challenge</div>
    <div class="submit">SEND INQUIRY</div>
    <p class="note">This demo form opens an email draft so the static site can be submitted without a backend.</p>
  </div>
</section>

<footer class="footer">
  <div class="fbrand"><i></i><span>Tallgrove Vale</span></div>
  <p class="tag">Property management for Cleveland, Akron, and Northeast Ohio owners.</p>
  <div class="fcol" style="left:639px"><h4>NAVIGATE</h4>Services<br>Owners<br>Process</div>
  <div class="fcol" style="left:866px"><h4>CONTACT</h4>Email<br>Request proposal</div>
  <div class="fbottom">© 2026 Tallgrove Vale Management LLC. All rights reserved.</div>
</footer>

</body>
</html>
```